Redesign of existing business card

I would like the "signage" attachment converted into a business card. This needs to be double sided aswell, keeping the phone number and names on the front, and the email + website on the back.

Second attachment is the current business card design.

Larger font for contact details is required.

Must keep to original color themes (electric blue, silver/grey etc)

Back of the card to have blue background with white writing.

Industry/Entity Type

Business

Contact Information for Business Card

Refer to existing design from attachments

Requirements
Must have
• Refer to existing design from attachments
Nice to have

```html
<!DOCTYPE html>
<html lang="en">
<head>
<meta charset="utf-8">
<title>Voltra Electro Services – Business Card</title>
<link href="https://fonts.googleapis.com/css2?family=Questrial&display=swap" rel="stylesheet">
<style>
  :root {
    --electric-blue: #3439a0;
    --electric-blue-deep: #2c3190;
    --silver: #a9abb1;
    --ink-grey: #5c5e66;
    --white: #ffffff;
    --backdrop: #ecebe8;
  }
  * { box-sizing: border-box; margin: 0; padding: 0; }
  html, body {
    width: 1200px; height: 700px; overflow: hidden;
    background: var(--backdrop);
    font-family: "Questrial", "Century Gothic", sans-serif;
  }
  .canvas {
    width: 1200px; height: 700px;
    display: flex; align-items: center; justify-content: center; gap: 60px;
  }
  .card {
    width: 520px; height: 318px; position: relative; overflow: hidden;
    border-radius: 4px;
    box-shadow: 0 6px 18px rgba(0,0,0,0.15);
  }

  /* Back side */
  .card--back {
    background: var(--electric-blue);
    color: var(--white);
  }
  .brand--back {
    position: absolute; top: 92px; left: 0; right: 0;
    display: flex; align-items: center; justify-content: center; gap: 14px;
  }
  .brand__dot {
    width: 40px; height: 40px; border-radius: 50%;
    border: 3px solid var(--white);
  }
  .brand__name {
    display: flex; flex-direction: column; line-height: 1;
    text-transform: uppercase; letter-spacing: 1px;
  }
  .brand__name-main { font-size: 44px; }
  .brand__name-sub { font-size: 15px; letter-spacing: 2px; margin-top: 4px; }
  .contact-list {
    position: absolute; left: 60px; right: 60px; top: 190px;
    list-style: none; font-size: 22px;
  }
  .contact-list__item {
    display: flex; align-items: center; gap: 12px; padding: 8px 0;
  }
  .contact-list__item + .contact-list__item {
    border-top: 1px solid rgba(255,255,255,0.55);
  }
  .contact-list__icon {
    width: 22px; height: 22px; flex: none;
    background: var(--white); border-radius: 3px;
    display: flex; align-items: center; justify-content: center;
  }

  /* Front side */
  .card--front { background: var(--white); }
  .brand--front {
    position: absolute; top: 34px; left: 36px;
    color: var(--electric-blue);
  }
  .brand--front .brand__name-main { font-size: 52px; letter-spacing: 2px; }
  .brand--front .brand__name-sub { font-size: 17px; letter-spacing: 2px; }
  .person {
    position: absolute; top: 150px; left: 40px; color: var(--ink-grey);
  }
  .person__name { font-size: 24px; }
  .person__role { font-size: 12px; margin-top: 3px; }
  .phone-tab {
    position: absolute; left: 0; top: 214px;
    width: 258px; height: 42px;
    background: var(--electric-blue);
    clip-path: polygon(0 0, 100% 0, 93% 100%, 0 100%);
    display: flex; align-items: center; gap: 10px; padding-left: 40px;
    color: var(--white); font-size: 22px; letter-spacing: 0.5px;
  }
</style>
</head>
<body>
<main class="canvas">

  <section class="card card--back" aria-label="Business card, back">
    <div class="brand brand--back">
      <span class="brand__dot"></span>
      <div class="brand__name">
        <span class="brand__name-main">Voltra</span>
        <span class="brand__name-sub">Electro Services</span>
      </div>
    </div>
    <ul class="contact-list">
      <li class="contact-list__item">
        <span class="contact-list__icon">
          <svg width="16" height="12" viewBox="0 0 16 12"><rect x="1" y="1" width="14" height="10" fill="none" stroke="#3439a0" stroke-width="1.6"/><path d="M1 1 L8 7 L15 1" fill="none" stroke="#3439a0" stroke-width="1.6"/></svg>
        </span>
        <span class="contact-list__text">dario@voltraelectro.com</span>
      </li>
      <li class="contact-list__item">
        <span class="contact-list__icon">
          <svg width="16" height="16" viewBox="0 0 16 16"><circle cx="8" cy="8" r="6.5" fill="none" stroke="#3439a0" stroke-width="1.5"/><ellipse cx="8" cy="8" rx="3" ry="6.5" fill="none" stroke="#3439a0" stroke-width="1.3"/><line x1="1.5" y1="8" x2="14.5" y2="8" stroke="#3439a0" stroke-width="1.3"/></svg>
        </span>
        <span class="contact-list__text">www.voltraelectro.com.au</span>
      </li>
    </ul>
  </section>

  <section class="card card--front" aria-label="Business card, front">
    <div class="brand brand--front">
      <div class="brand__name">
        <span class="brand__name-main">Voltra</span>
        <span class="brand__name-sub">Electro Services</span>
      </div>
    </div>
    <div class="person">
      <p class="person__name">Dario Kovac</p>
      <p class="person__role">Director | EC20461</p>
    </div>
    <div class="phone-tab">
      <svg width="20" height="20" viewBox="0 0 20 20" aria-hidden="true"><rect x="0" y="0" width="20" height="20" rx="4" fill="#ffffff"/><path d="M6 4.5 L8.2 4.5 L9 8 L7.6 9 Q9 12 11 12.4 L12 11 L15.5 11.8 L15.5 14 Q15.5 15.5 14 15.5 Q5 15 4.5 6 Q4.5 4.5 6 4.5 Z" fill="#3439a0"/></svg>
      <span class="phone-tab__text">Tel 0400 555 019</span>
    </div>
  </section>

</main>
</body>
</html>
```